WEBSITE: Security Officer Training, Security Officer Certifications, Security Officer Job Training

colorful and simple website, NO FLASH, and easy for SEO
Able to Upload to GODADDY WEBSITE BUILDER!

We need a great image that depicts and sell Harborline Watch Academy
Our websites for info: Security Officers doing cool things, the pictures must be great..

FEEL Free to choose ideas from our services in our
Www.harborlinewatchacademy.org site
The CPO certified protection officer tab
The CFO certified Firearms Office tab
The Security Officer Academy
The Campus security officer
Will be a few pages, landing page and contact page..
Www.harborlinewatchacademy.org
Www.civicwardenhall.net
Www.patrolcredentialhub.com
ALSO go to goggle and put in
Los Angles "Security Guard Training"
California Guard Card
Guard Card
Firearms Training
And similar words to see competitors websites!

WE want our more KICK ASS and COOOL!

OUr Industry: Security Officer Training Certifications
INFO: SECURITY OFFICER TRAINING
Law Enforcement
Police
Criminal Justice Training
Security Guards
Security Professional

Target Market(s)

Law Enforcement Training
Police Training
Criminal Justice Training
Security Officer Training
Security Officer Certifications

Industry/Entity Type

Security

Number of Pages Required

3 page

Requirements
Must have
• Able to upload to GODADDY WEBSITE BUILDER
• Easy to edit
• Must be easy for SEO
• NO FLASH or other things that prevent mobile phones
• MOBILE PHONE COMPATIBLE
• COOL!
• Call to action
• Contact form for email sign ups
• PICTURES SLIDE SHOW MUST HAVE
Should not have
• NO have flash

```html
<!DOCTYPE html>
<html lang="en">
<head>
<meta charset="utf-8">
<title>Harborline Watch Academy – Security Guard Training</title>
<link rel="stylesheet" href="https://fonts.googleapis.com/css2?family=Roboto:wght@400;500;700&family=Oswald:wght@400;500&display=swap">
<style>
:root{
  --bg-dark:#2b1e18;
  --gold:#c8996a;
  --gold-soft:#d3ab80;
  --maroon:#6e0f0f;
  --maroon-deep:#4d0a0a;
  --red-accent:#9b1414;
  --white:#ffffff;
  --ink:#222222;
  --grey-text:#777777;
  --panel-black:rgba(12,8,6,.88);
  --footer-bar:#0c0a09;
}
*{margin:0;padding:0;box-sizing:border-box}
html,body{width:698px;height:1200px;overflow:hidden}
body{
  position:relative;
  font-family:"Roboto",Arial,sans-serif;
  color:var(--white);
  background:
    radial-gradient(ellipse at 20% 30%,rgba(70,50,40,.35),transparent 60%),
    radial-gradient(ellipse at 80% 70%,rgba(60,40,32,.35),transparent 60%),
    var(--bg-dark);
}
.abs{position:absolute}

/* top bar */
.topbar{top:17px;left:51px;width:597px;height:14px;font-size:8.5px}
.topbar .item{position:absolute;top:2px;display:flex;align-items:center;gap:4px;white-space:nowrap}
.topbar svg{width:8px;height:8px;fill:var(--white)}
.social{position:absolute;right:0;top:3px;display:flex;gap:4px}
.social span{width:8px;height:8px;background:var(--white);border-radius:1px}

/* nav */
.nav{top:41px;left:51px;width:597px;height:40px;background:var(--gold)}
.nav a{position:absolute;top:0;height:40px;line-height:40px;font-size:8.4px;color:var(--white);text-decoration:none;text-transform:uppercase;white-space:nowrap}
.nav a.active{left:0;width:53px;text-align:center;background:linear-gradient(var(--maroon-deep),#2a0606)}
.brand{position:absolute;left:211px;top:-30px;width:70px;display:flex;flex-direction:column;align-items:center;z-index:2}
.brand .seal{width:58px;height:58px;border-radius:50%;background:var(--gold-soft);border:3px solid #e8d7bf}
.brand .name{margin-top:3px;font-size:6px;line-height:7.5px;font-weight:500;color:var(--white);text-transform:uppercase;text-align:center}

/* hero */
.hero{top:81px;left:51px;width:597px;height:311px;
  background:linear-gradient(100deg,#3d4a2c 0%,#6f7d5c 25%,#a7a9a3 55%,#c9cbc7 75%,#8c8e84 100%)}
.hero .caption{position:absolute;left:334px;top:176px;width:263px;height:74px;background:var(--panel-black);
  font-family:"Oswald",sans-serif;font-size:22px;line-height:28px;text-align:right;padding:8px 16px 0 0;text-transform:uppercase;white-space:nowrap;letter-spacing:-.2px}
.hero .arrows{position:absolute;top:272px;left:541px;display:flex;gap:6px}
.hero .arrows span{width:20px;height:20px;border-radius:50%;background:rgba(30,30,30,.8);display:flex;align-items:center;justify-content:center}
.hero .arrows svg{width:8px;height:8px;stroke:var(--white);stroke-width:2;fill:none}

/* campus block */
.campus{top:402px;left:50px;width:598px;height:142px;background:rgba(15,10,8,.55)}
.campus .photo{position:absolute;left:0;top:0;width:183px;height:142px;background:linear-gradient(#dfe6ee,#b9c1c7 70%,#8a8174)}
.campus h2{position:absolute;left:201px;top:16px;font-size:16px;font-weight:500;text-transform:uppercase}
.campus p{position:absolute;left:201px;top:42px;width:380px;font-size:8.3px;line-height:13.4px}
.campus .btn{position:absolute;left:205px;top:104px;width:60px;height:19px;border:1px solid var(--white);border-radius:2px;font-size:8px;line-height:17px;text-align:center}

/* services */
.services{top:552px;left:51px;width:597px;height:204px;background:var(--white);color:var(--ink);overflow:hidden}
.services h2{position:absolute;top:19px;width:100%;text-align:center;font-size:15px;font-weight:500;text-transform:uppercase}
.services h2 em{font-style:normal;color:var(--red-accent)}
.svc{position:absolute;top:52px;text-align:center;padding:0 10px}
.svc .ring{margin:0 auto;width:64px;height:64px;border-radius:50%;border:2px solid #e6ddd3;display:flex;align-items:center;justify-content:center;box-shadow:0 1px 3px rgba(0,0,0,.15)}
.svc .ring span{width:56px;height:56px;border-radius:50%;background:var(--gold);display:flex;align-items:center;justify-content:center}
.svc svg{width:24px;height:24px}
.svc h3{margin-top:16px;font-size:9px;font-weight:500;text-transform:uppercase}
.svc p{margin-top:6px;font-size:6.3px;line-height:10px;color:var(--grey-text)}
.divider{position:absolute;top:53px;width:1px;height:129px;background:#e2e2e2}

/* video */
.video{top:764px;left:51px;width:597px;height:246px;background:linear-gradient(var(--maroon),#5a0b0b)}
.video h2{position:absolute;top:13px;width:100%;text-align:center;font-size:15px;font-weight:500;text-transform:uppercase}
.vcard{position:absolute;top:39px;width:189px;height:184px;background:#0d0d0d}
.vcard .thumb{height:141px;display:flex;align-items:center;justify-content:center}
.vcard .play{width:38px;height:38px}
.vcard p{padding:10px 11px 0;font-size:7px;line-height:12.5px}

/* footer */
.footer{top:1020px;left:0;width:698px;height:132px;background:rgba(20,14,11,.45)}
.f-brand{position:absolute;left:54px;top:22px;width:74px;display:flex;flex-direction:column;align-items:center}
.f-brand .seal{width:56px;height:56px;border-radius:50%;background:var(--gold-soft);border:3px solid #e8d7bf}
.f-brand .name{margin-top:5px;font-size:6px;font-weight:500;text-align:center;line-height:8px;text-transform:uppercase}
.fcol{position:absolute;top:25px}
.fcol h4{font-size:9px;font-weight:400;text-transform:uppercase;margin-bottom:11px}
.fcol p{font-size:6.4px;line-height:9.7px}
.news-form{display:flex;margin-top:9px}
.news-form .field{width:85px;height:18px;background:var(--white);color:#888;font-size:6.5px;line-height:18px;padding-left:7px}
.news-form .go{width:32px;height:18px;background:var(--red-accent);font-size:6.8px;line-height:18px;text-align:center}

.copyright{top:1152px;left:0;width:698px;height:48px;background:var(--footer-bar);font-size:6.5px;text-align:center;line-height:48px}
</style>
</head>
<body>

<header class="abs topbar">
  <div class="item" style="left:2px">
    <svg viewBox="0 0 10 10"><rect x="0" y="0" width="10" height="10" rx="2"/><path d="M3 2.5l1 1.5-.6.6c.4.8 1 1.4 1.8 1.8l.6-.6 1.5 1-.6 1.2C4.8 7.8 2.4 5.4 2.2 3.2z" fill="#2b1e18"/></svg>
    (562) 410-2275
  </div>
  <div class="item" style="left:88px">
    <svg viewBox="0 0 10 8"><rect width="10" height="8" rx="1"/><path d="M0 0l5 4 5-4" stroke="#2b1e18" fill="none"/></svg>
    hello@harborlinewatch.org
  </div>
  <div class="item" style="left:364px">
    <svg viewBox="0 0 8 10"><path d="M4 0a3.5 3.5 0 0 1 3.5 3.5C7.5 6 4 10 4 10S.5 6 .5 3.5A3.5 3.5 0 0 1 4 0z"/><circle cx="4" cy="3.5" r="1.3" fill="#2b1e18"/></svg>
    2180 E. Marlow Ave Bellcrest, CA 90281
  </div>
  <div class="social"><span></span><span></span></div>
</header>

<nav class="abs nav">
  <a href="#" class="active">Home</a>
  <a href="#" style="left:60px">CaliforniaGuardCard</a>
  <a href="#" style="left:177px">FirearmsTraining</a>
  <div class="brand" style="left:262px"><span class="seal"></span><span class="name">Harborline<br>Watch Academy</span></div>
  <a href="#" style="left:338px">Security Officer Academy</a>
  <a href="#" style="left:471px">Security Jobs</a>
  <a href="#" style="left:551px">Contact</a>
</nav>

<section class="abs hero" role="img" aria-label="Slide photo: uniformed security officer standing in front of a patrol car">
  <div class="caption">Security Guard Training<br>in Los Angeles</div>
  <div class="arrows">
    <span><svg viewBox="0 0 8 8"><path d="M5.5 1L2.5 4l3 3"/></svg></span>
    <span><svg viewBox="0 0 8 8"><path d="M2.5 1l3 3-3 3"/></svg></span>
  </div>
</section>

<section class="abs campus">
  <div class="photo" role="img" aria-label="Photo: campus security officer standing on a paved lot"></div>
  <h2>CSO Campus Security Officer</h2>
  <p>TheCampus Security Officer (CSO)program is designed for officers entry into working with school districts K-12, Community College Campuses, Colleges or Universities. Work in the Campus Safety Department... This course meets the requirements for SB 1626 training to become a Campus Security Officer in the State of California. Program includes the California Guard Card in Los Angeles.</p>
  <div class="btn">Learn More</div>
</section>

<section class="abs services">
  <h2>Our <em>Service</em></h2>
  <div class="svc" style="left:0;width:147px">
    <div class="ring"><span><svg viewBox="0 0 24 24" fill="none" stroke="#fff" stroke-width="1.6"><rect x="3" y="5" width="18" height="16" rx="1"/><path d="M3 10h18M8 3v4M16 3v4M7 13h2M11 13h2M15 13h2M7 17h2M11 17h2M15 17h2"/></svg></span></div>
    <h3>Convenient!</h3>
    <p>Courses that fit your schedule, NOT the instructor's! -Morning and Afternoon Sessions available! Start Any Time!</p>
  </div>
  <div class="divider" style="left:147px"></div>
  <div class="svc" style="left:148px;width:151px">
    <div class="ring"><span><svg viewBox="0 0 24 24" fill="none" stroke="#fff" stroke-width="1.6"><rect x="2" y="6" width="20" height="12" rx="1"/><circle cx="12" cy="12" r="3"/></svg></span></div>
    <h3>Affordable!</h3>
    <p>We make your training affordable! Start and get your certifications.</p>
  </div>
  <div class="divider" style="left:299px"></div>
  <div class="svc" style="left:300px;width:151px">
    <div class="ring"><span><svg viewBox="0 0 24 24" fill="none" stroke="#fff" stroke-width="1.6"><path d="M12 3l2.7 5.6 6.1.8-4.5 4.2 1.1 6-5.4-2.9-5.4 2.9 1.1-6-4.5-4.2 6.1-.8z"/></svg></span></div>
    <h3>Valuable!</h3>
    <p>California guard card in Los Angeles. Get the skills for a New Career in Public Safety! while getting your security</p>
  </div>
  <div class="divider" style="left:451px"></div>
  <div class="svc" style="left:452px;width:145px">
    <div class="ring"><span><svg viewBox="0 0 24 24" fill="#fff"><path d="M12 3c1 4 5 6 5 10a5 5 0 0 1-10 0c0-2 1-3 2-4 0 2 1 3 2 3-1-3 0-6 1-9z"/><rect x="6" y="20" width="12" height="1.5"/></svg></span></div>
    <h3>Fast</h3>
    <p>-1 day security guard training in Los Angeles! Start at 8am and done the same day in the afternoon!</p>
  </div>
</section>

<section class="abs video">
  <h2>Our Video</h2>
  <div class="vcard" style="left:11px">
    <div class="thumb" role="img" aria-label="Video still: officer in a dark jacket holding a radio" style="background:linear-gradient(120deg,#6b5a4a,#1e2a40 60%,#3c3a3a)">
      <svg class="play" viewBox="0 0 40 40"><circle cx="20" cy="20" r="18" fill="rgba(255,255,255,.15)" stroke="rgba(255,255,255,.6)" stroke-width="1.5"/><path d="M16 13l11 7-11 7z" fill="rgba(255,255,255,.7)"/></svg>
    </div>
    <p>Sed ut perspiciatis unde omnis iste natus error sit voluptatem accusantium doloremque</p>
  </div>
  <div class="vcard" style="left:204px">
    <div class="thumb" role="img" aria-label="Video still: guard in a cap with arms crossed at a glass entrance" style="background:linear-gradient(120deg,#8aa0a8,#d8dde0 40%,#1b1c20 75%)">
      <svg class="play" viewBox="0 0 40 40"><circle cx="20" cy="20" r="18" fill="rgba(255,255,255,.15)" stroke="rgba(255,255,255,.6)" stroke-width="1.5"/><path d="M16 13l11 7-11 7z" fill="rgba(255,255,255,.7)"/></svg>
    </div>
    <p>Sed ut perspiciatis unde omnis iste natus error sit voluptatem accusantium doloremque</p>
  </div>
  <div class="vcard" style="left:396px">
    <div class="thumb" role="img" aria-label="Video still: officer's duty belt against a city skyline" style="background:linear-gradient(180deg,#9fc3e0,#bcd6ea 50%,#4d5560 85%)">
      <svg class="play" viewBox="0 0 40 40"><circle cx="20" cy="20" r="18" fill="rgba(255,255,255,.15)" stroke="rgba(255,255,255,.6)" stroke-width="1.5"/><path d="M16 13l11 7-11 7z" fill="rgba(255,255,255,.7)"/></svg>
    </div>
    <p>Sed ut perspiciatis unde omnis iste natus error sit voluptatem accusantium doloremque</p>
  </div>
</section>

<footer class="abs footer">
  <div class="f-brand"><span class="seal"></span><span class="name">Harborline<br>Watch Academy</span></div>
  <div class="fcol" style="left:175px;width:143px">
    <h4>Neque Porro Quisquam</h4>
    <p>Lorem Ipsum has been the industry's standard dummy text ever since the 1500s, when an unknown printer took a galley of type</p>
    <p style="margin-top:9px">&nbsp;It has survived not only five centuries, but also the leap into electronic typesetting, remaining essentially unchanged</p>
  </div>
  <div class="fcol" style="left:382px;width:110px">
    <h4>Get In Touch</h4>
    <p>Address : 715 Quarry Lane,<br>Bellcrest, CA</p>
    <p style="margin-top:10px">Phone : (562)4108830</p>
    <p style="margin-top:10px">Email : Info@harborlinewatch.org</p>
  </div>
  <div class="fcol" style="left:531px;width:120px">
    <h4>Newsletter</h4>
    <p>Your about us information would fit<br>here nicely.</p>
    <div class="news-form"><div class="field">Email address</div><div class="go">Submit</div></div>
  </div>
</footer>

<div class="abs copyright">Copyright © 2016. All Rights Reserved</div>

</body>
</html>
```